CONTACT US Page and design for website

We need a contact us page for our website. We would like it to have a message area, a map, our information, etc.

Please see the text attachment for what we are looking for. We need to have something that is creative and interesting, modern and professional.

We believe that a contact US page should be very creative because everyone clicks that to contact us. We want it to be super professional, attention grabbing, pleasing to the eye.

PLEASE KEEP THE HEADER AND FOOTER THE SAME, ONLY THE ACTUAL CONTACT US PAGE NEEDS TO BE WORKED ON. THANKS!
We are excited to work with designers for this project.

Target Market(s)

Clients in technology business

Industry/Entity Type

Information Technology

Number of Pages Required

1 page

Font styles to use
Serif

Requirements
Must have
• CHECK THE TEXT ATTACHMENT PLEASE
• Must stay within our design colors and theme.
Nice to have
• see attachment
Should not have
• it should be special

```html
<!DOCTYPE html>
<html lang="en">
<head>
<meta charset="utf-8">
<title>Contact Us – Novarig Systems</title>
<link href="https://fonts.googleapis.com/css2?family=Arimo:wght@400;700&display=swap" rel="stylesheet">
<style>
:root{
  --teal:#2aa89f;
  --teal-light:#3ecdbf;
  --teal-dark:#1f8f87;
  --ink:#222;
  --muted:#888;
  --line:#e2e2e2;
  --soft:#f6f6f6;
  --footer:#a6a6a6;
  --footer-dark:#9a9a9a;
  --white:#fff;
}
*{box-sizing:border-box;margin:0;padding:0}
html,body{width:922px;height:1200px;overflow:hidden;background:var(--white)}
body{font-family:"Arimo",Arial,sans-serif;color:var(--ink);position:relative}
.abs{position:absolute}
/* header */
.site-header{position:absolute;left:0;top:0;width:922px;height:83px;border-bottom:1px solid var(--line)}
.brand{left:48px;top:22px;display:flex;align-items:center;gap:10px}
.brand-mark{width:30px;height:30px;border-radius:50%;background:var(--teal)}
.brand-name{font-size:24px;color:var(--teal);letter-spacing:2px}
.account{left:716px;top:0;width:158px;height:28px;border-radius:0 0 18px 18px;overflow:hidden;display:flex;font-size:9px}
.account span{flex:1;display:flex;align-items:center;justify-content:center;color:#333}
.account .signup{background:#b9b9b9}
.account .login{background:#9c9c9c}
.quick{top:40px;display:flex;align-items:center;gap:8px}
.icon-ring{width:32px;height:32px;border-radius:50%;border:1px solid #ddd;background:#f4f4f4;display:flex;align-items:center;justify-content:center}
.live-chat{left:628px;font-size:11px}
.hotline{left:739px;font-size:15px}
.main-nav{left:45px;top:96px;display:flex;gap:21px;font-size:9px;color:#444}
.search{left:715px;top:92px;width:126px;height:27px;border:1px solid #999;border-radius:14px;font-size:9px;padding:0 0 0 16px;display:flex;align-items:center;justify-content:space-between;padding-right:8px}
.cart{left:849px;top:90px;width:30px;height:30px;border-radius:50%;border:1px solid #999;display:flex;align-items:center;justify-content:center}
/* banner */
.crumb-bar{left:0;top:123px;width:922px;height:30px;background:linear-gradient(90deg,var(--teal-dark),var(--teal-light) 50%,var(--teal-dark));font-size:10.5px;color:var(--white);padding:9px 0 0 98px}
.crumb-bar b{font-weight:400;color:#111}
.hero{left:0;top:153px;width:922px;height:100px;background:linear-gradient(90deg,#3aa9a2,#6fc6c0 50%,#48b0a9)}
.hero-title{left:0;top:194px;width:922px;text-align:center;color:var(--white);font-size:14px}
/* inquiries */
.inquiries{left:0;top:253px;width:922px;height:178px;background:var(--soft)}
.inquiry{top:294px;width:160px;text-align:center;font-size:8.5px;line-height:17px}
.inquiry strong{display:block}
/* card */
.contact-card{left:165px;top:369px;width:592px;height:282px;background:var(--white);box-shadow:0 4px 12px rgba(0,0,0,.18);display:flex}
.message-form{width:372px;position:relative;padding:33px 24px 0}
.panel-title{font-size:11px;color:var(--teal)}
.hours .panel-title{color:var(--white)}
.field{position:absolute;font-size:6px;color:var(--muted);border-bottom:1px solid var(--line);height:28px}
.send-btn{position:absolute;left:318px;top:229px;width:28px;height:28px;border-radius:50%;background:var(--teal);display:flex;align-items:center;justify-content:center}
.hours{flex:1;background:var(--teal);color:var(--white);padding:33px 26px 0;position:relative;overflow:hidden}
.hours ul{list-style:none;margin:23px 0 0 8px;font-size:7.3px;line-height:16.8px}
.social{display:flex;gap:9px;margin:18px 0 0 8px}
.social i,.foot-social i{display:block;border-radius:50%}
.social i{width:10px;height:10px;border:1.3px solid #b8ece7}
/* office */
.office-title{left:178px;top:773px;font-size:15px;font-weight:700;color:var(--teal)}
.office-address{left:180px;top:803px;font-size:8.5px;line-height:16.5px;color:#444}
.map{left:337px;top:714px;width:421px;height:169px;background:linear-gradient(135deg,#ececec,#e2e2e2);box-shadow:0 2px 6px rgba(0,0,0,.2)}
/* footer */
.site-footer{left:0;top:939px;width:922px;height:161px;background:var(--footer);color:var(--white)}
.footer-blurb{left:270px;top:948px;width:420px;text-align:center;font-size:7.5px;line-height:11px;color:var(--white)}
.footer-rule{height:1px;background:rgba(255,255,255,.35)}
.footer-contact{top:1010px;font-size:8px;color:var(--white);display:flex;gap:6px;line-height:11px}
.footer-links{left:238px;top:1050px;display:flex;gap:40px;font-size:9px;color:var(--white)}
.support-links{left:600px;top:1063px;width:80px;text-align:center;font-size:5.5px;line-height:8px;color:var(--white)}
.footer-bottom{left:0;top:1100px;width:922px;height:100px;background:var(--footer-dark)}
.foot-social{left:400px;top:1111px;display:flex;gap:8px}
.foot-social i{width:21px;height:21px;border:1px solid rgba(255,255,255,.8)}
.copyright{left:420px;top:1154px;font-size:7px;line-height:9px;color:var(--white);display:flex;gap:6px;align-items:center}
.chat-now{left:797px;top:1185px;width:117px;height:15px;background:var(--teal-light);color:var(--white);font-size:7px;font-weight:700;padding:3px 6px;display:flex;justify-content:space-between;font-family:Georgia,serif}
</style>
</head>
<body>
<header class="site-header">
  <div class="abs brand"><span class="brand-mark"></span><span class="brand-name">NOVARIG</span></div>
  <div class="abs account"><span class="signup">SIGN UP</span><span class="login">LOGIN</span></div>
  <div class="abs quick live-chat"><span class="icon-ring"><svg width="12" height="10" viewBox="0 0 12 10"><path d="M1 1h10v6H5l-3 2V7H1z" fill="#2aa89f"/></svg></span>LIVE CHAT</div>
  <div class="abs quick hotline"><span class="icon-ring"><svg width="11" height="11" viewBox="0 0 12 12"><path d="M2 1l2 0 1 3-1.5 1a7 7 0 003.5 3.5L8 7l3 1v2a1 1 0 01-1 1A9 9 0 011 2a1 1 0 011-1z" fill="#2aa89f"/></svg></span>555-014-2200</div>
</header>
<nav class="abs main-nav"><span>SERVERS</span><span>WORKSTATIONS</span><span>COMPONENTS</span><span>VIRTUAL REALITY</span><span>DRONES</span><span>ABOUT US</span><span>BLOG</span><span>RESOURCES</span><span>CONTACT US</span></nav>
<div class="abs search">Search<svg width="12" height="12" viewBox="0 0 12 12"><circle cx="5" cy="5" r="3.8" fill="none" stroke="#2aa89f" stroke-width="1.6"/><path d="M8 8l3 3" stroke="#2aa89f" stroke-width="1.8"/></svg></div>
<div class="abs cart"><svg width="14" height="11" viewBox="0 0 14 11"><path d="M1 3h12l-1.5 7h-9z" fill="#2aa89f"/><path d="M4 3l3-2 3 2" stroke="#2aa89f" fill="none"/></svg></div>

<div class="abs crumb-bar">HOME / <b>CONTACT US</b></div>
<div class="abs hero" role="img" aria-label="Teal-tinted photo of a desk with keyboard, mouse and laptop"></div>
<h1 class="abs hero-title" style="font-weight:400">CONTACT INFORMATIONS</h1>

<section class="abs inquiries"></section>
<div class="abs inquiry" style="left:177px"><strong>General Inquiries</strong>(555)014-2200<br>info@novarig.example</div>
<div class="abs inquiry" style="left:382px"><strong>Purchasing Inquiries</strong>(555)014-2201<br>purchasing@novarig.example</div>
<div class="abs inquiry" style="left:580px"><strong>Sales Inquiries</strong>(555)014-2200<br>sales@novarig.example</div>

<section class="abs contact-card">
  <form class="message-form">
    <h2 class="panel-title" style="font-weight:400">Send Us Message</h2>
    <svg class="abs" style="left:323px;top:31px" width="24" height="11" viewBox="0 0 24 11"><rect x="9" y="0" width="15" height="11" fill="#2aa89f"/><path d="M9 0l7.5 6L24 0" stroke="#fff" fill="none"/><path d="M0 3h7M2 6h5M4 9h3" stroke="#2aa89f"/></svg>
    <div class="field" style="left:24px;top:68px;width:140px">Your Name</div>
    <div class="field" style="left:206px;top:68px;width:140px">Email Address</div>
    <div class="field" style="left:24px;top:113px;width:140px">Phone Number</div>
    <div class="field" style="left:206px;top:113px;width:140px">Subject</div>
    <div class="field" style="left:24px;top:159px;width:322px">Message</div>
    <span class="send-btn"><svg width="14" height="12" viewBox="0 0 14 12"><path d="M1 6L13 1 10 11 7 7z" fill="none" stroke="#fff"/><path d="M7 7l6-6" stroke="#fff"/></svg></span>
  </form>
  <aside class="hours">
    <h2 class="panel-title" style="font-weight:400">Hours Of Operation</h2>
    <ul>
      <li>Monday: 8:00am- 5:00pm</li>
      <li>Tuesday: 8:00am- 5:00pm</li>
      <li>Wednesday: 8:00am- 5:00pm</li>
      <li>Thursday: 8:00am- 5:00pm</li>
      <li>Friday: 8:00am- 5:00pm</li>
      <li>Our dedicated customer service representatives</li>
      <li>are available 24/7 by phone.</li>
    </ul>
    <div class="social"><i></i><i></i><i></i><i></i></div>
  </aside>
</section>

<h2 class="abs office-title">Office Headquarters</h2>
<address class="abs office-address" style="font-style:normal">Novarig Systems, LLC.<br>4120 Halden Ave.<br>Larkfield, CA 90000</address>
<div class="abs map" role="img" aria-label="Street map showing the office location"></div>

<footer class="abs site-footer"></footer>
<p class="abs footer-blurb">Based in Larkfield California, Novarig Systems offers custom servers, storage, and workstations for local businesses in Los Angeles, Beverly Hills, Thousand Oaks, Ventura, Orange County, Santa Barbara, Oxnard, Irvine, Anaheim, and San Diego. Novarig Systems also offers such products to clients throughout the United States and Worldwide.</p>
<div class="abs footer-rule" style="left:275px;top:999px;width:410px"></div>
<div class="abs footer-contact" style="left:286px"><svg width="7" height="9" viewBox="0 0 7 9"><path d="M3.5 9C1 5.5 0 4.5 0 3.5a3.5 3.5 0 017 0C7 4.5 6 5.5 3.5 9z" fill="#fff"/><circle cx="3.5" cy="3.5" r="1.2" fill="#a6a6a6"/></svg><span>4120 Halden Ave.<br>&nbsp;&nbsp;&nbsp;Larkfield, CA 90000</span></div>
<div class="abs footer-contact" style="left:431px"><svg width="8" height="8" viewBox="0 0 12 12"><path d="M2 1l2 0 1 3-1.5 1a7 7 0 003.5 3.5L8 7l3 1v2a1 1 0 01-1 1A9 9 0 011 2a1 1 0 011-1z" fill="#fff"/></svg><span>555-014-2200</span></div>
<div class="abs footer-contact" style="left:556px"><svg width="9" height="7" viewBox="0 0 9 7"><rect width="9" height="7" fill="#fff"/><path d="M0 0l4.5 4L9 0" stroke="#a6a6a6" fill="none"/></svg><span>sales@novarig.example</span></div>
<nav class="abs footer-links"><span>Computer Hardware</span><span>Drones</span><span>Virtual Reality</span><span>About Us</span><span>Customer Support</span></nav>
<div class="abs support-links">Terms and Conditions<br>Warranty Information<br>Contact Us<br>Return Policy</div>
<div class="abs footer-bottom"></div>
<div class="abs foot-social"><i></i><i></i><i></i><i></i></div>
<div class="abs footer-rule" style="left:130px;top:1144px;width:680px"></div>
<div class="abs copyright"><span>Novarig Systems, LLC.<br>Copyright © 2017</span></div>
<div class="abs chat-now"><span>CHAT NOW</span><span>^</span></div>
</body>
</html>
```